Business Card needed for Drainor, a growing Septic Service company

Drainor, a growing local septic service company in Pennsylvania, needs updated business cards. We'd like the business card to feature our logo and communicate that we provide Septic Pumping, Installations/Repairs, Restroom Rentals, and 24/7 Emergency Service. The business card should be eye-catching, bold, and clean/simple. We have been in business almost 10 years and would like to expand and update our business brand and image.

Target Market(s)

Residential and Commercial, New and Current Homeowners

Industry/Entity Type

Service

Contact Information for Business Card

Contact on the business card should be: Dean Harlow Owner & Operator
Phone: 610-555-0187
Email: service@drainor-example.com
Website: www.drainor-example.com
Address: 812 Millbrook Lane Easton PA 18042

Font styles to use
Sans Serif

Colors

Designer to choose colors to be used in the design.

Requirements
Must have
• Feature logo on both side of business card.
Nice to have
• We envision the contact information on one side and our services listed on the other side. Utilize the green from the symbol in our logo as part of the design, overall design color scheme should be white, grey, black.

```html
<!DOCTYPE html>
<html lang="en">
<head>
<meta charset="utf-8">
<title>Drainor Business Card – Services Side</title>
<link rel="stylesheet" href="https://fonts.googleapis.com/css2?family=Archivo:wght@700;800&family=Arimo:wght@400&display=swap">
<style>
  :root {
    --charcoal: #20272a;
    --lime: #6cc417;
    --lime-frame: #86e01e;
    --white: #ffffff;
  }
  html, body {
    margin: 0;
    padding: 0;
    overflow: hidden;
    background: var(--charcoal);
  }
  .card {
    position: relative;
    width: 1200px;
    height: 685px;
    background: var(--charcoal);
    overflow: hidden;
    font-family: "Archivo", "Arial", sans-serif;
  }
  .card-frame {
    position: absolute;
    left: 23px;
    top: 31px;
    width: 1147px;
    height: 619px;
    border: 3px solid var(--lime-frame);
    box-sizing: border-box;
  }
  .service-band {
    position: absolute;
    left: 0;
    top: 229px;
    width: 100%;
    height: 227px;
    background: var(--lime);
  }
  .service-list {
    position: absolute;
    left: 100px;
    top: 285px;
    margin: 0;
    padding: 0;
    list-style: none;
    display: grid;
    grid-template-columns: 512px auto;
    row-gap: 25px;
    color: var(--white);
    font-weight: 700;
    font-size: 36px;
    letter-spacing: 0.6px;
    line-height: 42px;
  }
  .service-list li {
    display: flex;
    align-items: center;
  }
  .service-list li::before {
    content: "";
    width: 14px;
    height: 14px;
    border-radius: 50%;
    background: var(--white);
    margin-right: 12px;
    flex-shrink: 0;
  }
  .brand {
    position: absolute;
    right: 100px;
    top: 512px;
    text-align: right;
    color: var(--white);
  }
  .brand-name {
    display: flex;
    align-items: center;
    justify-content: flex-end;
    gap: 12px;
    font-weight: 800;
    font-size: 44px;
    letter-spacing: 2px;
    line-height: 1;
    text-transform: uppercase;
  }
  .brand-mark {
    width: 38px;
    height: 38px;
    background: var(--lime);
  }
  .brand-url {
    margin-top: 8px;
    font-family: "Arimo", "Arial", sans-serif;
    font-size: 25px;
    letter-spacing: 0.3px;
  }
</style>
</head>
<body>
  <main class="card">
    <div class="card-frame"></div>
    <div class="service-band"></div>
    <ul class="service-list">
      <li>Septic Pumping</li>
      <li>Restroom Rentals</li>
      <li>Installations/Repairs</li>
      <li>24/7 Emergency Service</li>
    </ul>
    <div class="brand">
      <div class="brand-name"><span class="brand-mark"></span>Drainor</div>
      <div class="brand-url">www.drainor-example.com</div>
    </div>
  </main>
</body>
</html>
```